Business Card for a Mortgage Agent (myself)

I need a business card for my new job as Mortgage Agent. The Broker's logo is to be on the card as well as the brokerage License number. Not sure if to include a photo or not. Info to be on card.
Dante Roux
Mortgage Agent
Lic # M47105386
Cell: 905-614-2753
Email: danterouxk.ma@fennmail.com
Web: www.karlvostermortgages.com
TPW Brokerage Lic. # 73918

```html
<!DOCTYPE html>
<html lang="en">
<head>
<meta charset="utf-8">
<title>Dante Roux – Mortgage Agent Business Card</title>
<link rel="stylesheet" href="https://fonts.googleapis.com/css2?family=Jost:wght@500&family=Inter:ital,wght@0,400;1,400&display=swap">
<style>
  :root {
    --brand-blue: #064f93;
    --brand-yellow: #fdc90c;
    --brand-yellow-deep: #f2bd08;
    --paper: #ffffff;
    --backdrop: #e9e9e9;
    --text-light: #ffffff;
  }
  * { margin: 0; padding: 0; box-sizing: border-box; }
  html, body {
    width: 1200px; height: 790px; overflow: hidden;
    background: var(--backdrop);
  }
  .canvas { position: relative; width: 1200px; height: 790px; }
  .card {
    position: absolute; top: 232px;
    width: 480px; height: 274px; overflow: hidden;
  }
  .card--front { left: 103px; background: var(--paper); }
  .card--back { left: 611px; background: var(--brand-blue); }

  .brand {
    position: absolute; left: 32px; top: 108px;
    display: flex; align-items: center; gap: 9px;
    z-index: 2;
  }
  .brand__mark {
    width: 14px; height: 14px; background: var(--brand-yellow);
  }
  .brand__name {
    font-family: "Jost", sans-serif; font-weight: 500;
    font-size: 18px; letter-spacing: 0.04em; text-transform: uppercase;
    color: var(--brand-blue); white-space: nowrap;
  }

  .decor-area { position: absolute; top: 0; height: 274px; }
  .card--front .decor-area {
    left: 0; width: 480px;
    background: linear-gradient(135deg, var(--brand-yellow) 0%, var(--brand-yellow-deep) 100%);
    clip-path: polygon(330px 0, 480px 0, 480px 274px, 290px 274px, 211px 199px, 310px 100px);
  }
  .card--back .decor-area {
    left: 0; width: 260px;
    background: linear-gradient(135deg, var(--brand-yellow) 0%, var(--brand-yellow-deep) 100%);
    clip-path: polygon(0 0, 190px 0, 260px 185px, 200px 274px, 0 274px);
  }

  .agent {
    position: absolute; right: 33px; top: 126px;
    text-align: right; color: var(--text-light);
    font-family: "Inter", sans-serif; font-size: 11.5px; line-height: 1.2;
  }
  .agent__name {
    font-family: "Jost", sans-serif; font-weight: 500;
    font-size: 18.5px; letter-spacing: 0.06em; text-transform: uppercase;
    color: var(--brand-yellow); margin-bottom: 1px;
  }
  .agent__title { font-size: 11.5px; }
  .agent__licence { font-style: italic; font-size: 11px; margin-top: 1px; }
  .contact { list-style: none; margin-top: 10px; margin-right: -13px; }
  .contact li {
    display: flex; justify-content: flex-end; align-items: center;
    gap: 5px; height: 13.5px;
  }
  .contact svg { width: 8px; height: 8px; fill: var(--brand-yellow); }
  .agent__brokerage { margin-top: 8px; }
</style>
</head>
<body>
<main class="canvas">
  <section class="card card--front">
    <div class="decor-area" role="img" aria-label="Decorative geometric pattern in yellow and blue"></div>
    <div class="brand">
      <span class="brand__mark"></span>
      <span class="brand__name">True Path Wealth</span>
    </div>
  </section>

  <section class="card card--back">
    <div class="decor-area" role="img" aria-label="Decorative geometric pattern in yellow and white"></div>
    <div class="agent">
      <h1 class="agent__name">Dante Roux</h1>
      <p class="agent__title">Mortgage Agent</p>
      <p class="agent__licence">LIC # M47105386</p>
      <ul class="contact">
        <li>905-614-2753
          <svg viewBox="0 0 10 10" aria-hidden="true"><path d="M2 0.5l2 2-1 1.2c.6 1.4 1.6 2.4 3 3l1.2-1 2 2-1.2 1.8C4.5 9.3.7 5.5.2 1.7z"/></svg>
        </li>
        <li>danterouxk.ma@fennmail.com
          <svg viewBox="0 0 10 10" aria-hidden="true"><path d="M0 2h10v6H0z M0 2l5 3.5L10 2" stroke="#064f93" stroke-width="0.8"/></svg>
        </li>
        <li>www.karlvostermortgages.com
          <svg viewBox="0 0 10 10" aria-hidden="true"><circle cx="5" cy="5" r="4.8"/><path d="M0.5 5h9M5 0.3c-2.5 2.8-2.5 6.6 0 9.4M5 0.3c2.5 2.8 2.5 6.6 0 9.4" stroke="#064f93" stroke-width="0.7" fill="none"/></svg>
        </li>
      </ul>
      <p class="agent__brokerage">TPW Brokerage Lic. # 73918</p>
    </div>
  </section>
</main>
</body>
</html>
```